Accountability Project Graphics

I want to create 10 social media graphics (new Instagram size 4:5 (1080 x 1350 pixels) focusing on our Kelmora Accountability App, using any of the 3 pictures attached. Use the attached pics only, NO RANDOM STOCK PHOTOGRAPHY. For the color scheme, use the landing page colors/fonts (attached).
You can add any of the 3 photos attached but I mainly need BOLD text that includes these headlines and sub-headlines on them.
Please NOTE for all the headlines below, also add this sub-headline on each graphic:
Stay Consistent with MB in Your Pocket!
Here are the headlines:
• Stop Starting Over Every Monday
• You don't need more willpower. You need more support
• Built for women who are tired of doing this alone
• When Motivation Fades, MB Checks In
• The Support System You've Been Missing
• Support When Motivation Disappears
• What if MB Checked in Every Day?
• The Missing Piece Isn't Another Diet
• Eat the food you love. Stay accountable every day.
• One Bad Meal Doesn't Mean You Failed
women over 40 trying to lose weight

```html
<!DOCTYPE html>
<html lang="en">
<head>
<meta charset="utf-8">
<title>Kelmora Accountability App – Social Graphics</title>
<link href="https://fonts.googleapis.com/css2?family=Lora:ital,wght@0,600;0,700;1,600;1,700&family=Montserrat:wght@500;700&display=swap" rel="stylesheet">
<style>
  :root{
    --page:#ffffff;
    --card:#fadbe3;
    --card-light:#fde9ee;
    --pink:#d9507f;
    --ink:#141414;
    --cloth:#2a2f3f;
    --device:#cfd2d8;
  }
  *{margin:0;padding:0;box-sizing:border-box}
  html,body{width:1200px;height:601px;overflow:hidden;background:var(--page)}
  .board{position:relative;width:1200px;height:601px}
  .card{position:absolute;width:230px;height:287px;background:linear-gradient(180deg,var(--card) 0%,var(--card-light) 55%,var(--card) 100%);overflow:hidden}
  .photo{position:absolute}
  .photo--solo{background:linear-gradient(180deg,#3b3440 0%,var(--cloth) 40%,rgba(42,47,63,.55) 72%,rgba(250,219,227,0) 100%)}
  .photo--hug{background:linear-gradient(160deg,#c9a9d6 0%,#e08aa8 35%,#f2e8dc 62%,rgba(250,219,227,0) 100%)}
  .photo--duo{background:linear-gradient(180deg,#2f3850 0%,#3e5577 45%,#cfd3de 72%,rgba(250,219,227,0) 100%)}
  .device{position:absolute;background:linear-gradient(180deg,#ffffff 0%,#f6e4ea 70%,var(--device) 88%,#a9adb5 100%);border-radius:4px;box-shadow:0 3px 6px rgba(0,0,0,.15)}
  .ghost{position:absolute;background:rgba(255,255,255,.35);border:1px solid rgba(217,80,127,.12);border-radius:3px;transform:rotate(12deg)}
  .headline{position:absolute;font-family:"Lora",Georgia,serif;font-weight:700;color:var(--ink);line-height:1.05}
  .headline .accent{color:var(--pink)}
  .headline em{font-style:italic;font-weight:600}
  .center{left:0;right:0;text-align:center}
  .tagline{position:absolute;left:0;right:0;text-align:center;font-family:"Montserrat",Arial,sans-serif;font-weight:500;font-size:7.3px;color:var(--ink)}
  .tagline b{font-weight:700}
</style>
</head>
<body>
<main class="board">

  <section class="card" style="left:12px;top:10px">
    <div class="ghost" style="left:150px;top:12px;width:80px;height:55px"></div>
    <div class="photo photo--solo" role="img" aria-label="Photo: smiling woman in black lace outfit, hand on hip" style="left:113px;top:30px;width:117px;height:257px"></div>
    <div class="device" role="img" aria-label="Laptop showing the Eat the Food You Love landing page" style="left:18px;top:168px;width:136px;height:100px;transform:rotate(-8deg)"></div>
    <h2 class="headline" style="left:10px;top:16px;width:114px;text-align:center;font-size:22px;line-height:1.05">
      <span class="accent">Stop<br>Starting<br>Over</span><br>Every<br>Monday
    </h2>
    <p class="tagline" style="left:10px;right:auto;width:114px;top:142px;line-height:1.35">Stay Consistent with<br>MB in Your Pocket!</p>
  </section>

  <section class="card" style="left:249px;top:10px">
    <div class="photo photo--hug" role="img" aria-label="Photo: two women sharing a joyful hug" style="left:13px;top:12px;width:204px;height:165px"></div>
    <h2 class="headline center" style="top:172px;font-size:21px">You don't need<br><em>more willpower.</em><br><span class="accent">You need<br><em>more support</em></span></h2>
    <p class="tagline" style="top:270px">Stay Consistent <b>with MB</b> in Your Pocket!</p>
  </section>

  <section class="card" style="left:485px;top:10px">
    <div class="ghost" style="left:140px;top:118px;width:80px;height:55px"></div>
    <h2 class="headline center" style="top:19px;font-size:22px;line-height:.97">Built for women<br>who are <em class="accent">tired</em><br><em class="accent">of doing this alone</em></h2>
    <p class="tagline" style="top:97px">Stay Consistent <b>with MB</b> in Your Pocket!</p>
    <div class="photo photo--duo" role="img" aria-label="Photo: two women laughing together in denim jackets" style="left:43px;top:109px;width:150px;height:178px"></div>
  </section>

  <section class="card" style="left:721px;top:10px">
    <div class="ghost" style="left:8px;top:170px;width:70px;height:50px;transform:rotate(-10deg)"></div>
    <div class="ghost" style="left:150px;top:130px;width:80px;height:55px"></div>
    <h2 class="headline center" style="top:20px;font-size:22px;line-height:.97">When<br>Motivation Fades,<br><em class="accent">MB Checks In</em></h2>
    <p class="tagline" style="top:97px">Stay Consistent <b>with MB</b> in Your Pocket!</p>
    <div class="photo photo--hug" role="img" aria-label="Photo: two women sharing a joyful hug" style="left:50px;top:120px;width:170px;height:167px"></div>
  </section>

  <section class="card" style="left:958px;top:10px">
    <div class="ghost" style="left:18px;top:80px;width:70px;height:55px;transform:rotate(-10deg)"></div>
    <div class="ghost" style="left:150px;top:15px;width:75px;height:55px"></div>
    <div class="photo photo--solo" role="img" aria-label="Photo: smiling woman in black lace outfit, hand on hip" style="left:42px;top:7px;width:156px;height:175px"></div>
    <h2 class="headline center" style="top:181px;font-size:25px;line-height:1">The Support<br>System <span class="accent">You've<br>Been Missing</span></h2>
    <p class="tagline" style="top:277px">Stay Consistent <b>with MB</b> in Your Pocket!</p>
  </section>

  <section class="card" style="left:12px;top:304px">
    <div class="photo photo--solo" role="img" aria-label="Photo: smiling woman in black lace outfit, hand on hip" style="left:138px;top:5px;width:92px;height:240px"></div>
    <div class="device" role="img" aria-label="Laptop showing the Eat the Food You Love landing page" style="left:20px;top:28px;width:108px;height:78px;transform:rotate(-6deg)"></div>
    <h2 class="headline" style="left:19px;top:124px;font-size:31px;line-height:1.05"><span class="accent">Support<br>When</span><br>Motivation<br><em>Disappears</em></h2>
    <p class="tagline" style="left:19px;right:auto;text-align:left;top:268px">Stay Consistent <b>with MB</b> in Your Pocket!</p>
  </section>

  <section class="card" style="left:249px;top:304px">
    <div class="ghost" style="left:10px;top:80px;width:60px;height:50px;transform:rotate(-10deg)"></div>
    <div class="photo photo--hug" role="img" aria-label="Photo: two women sharing a joyful hug" style="left:50px;top:8px;width:170px;height:170px"></div>
    <h2 class="headline center" style="top:176px;font-size:24px"><span class="accent">What if</span><br>MB Checked <span class="accent">in<br>Every Day?</span></h2>
    <p class="tagline" style="top:268px">Stay Consistent <b>with MB</b> in Your Pocket!</p>
  </section>

  <section class="card" style="left:485px;top:304px">
    <div class="ghost" style="left:140px;top:20px;width:80px;height:55px"></div>
    <div class="ghost" style="left:10px;top:120px;width:70px;height:50px;transform:rotate(-10deg)"></div>
    <h2 class="headline center" style="top:20px;font-size:37px;line-height:1.02"><span class="accent">The<br>Missing<br>Piece</span><br>Isn't<br>Another<br><span class="accent">Diet</span></h2>
    <p class="tagline" style="top:264px">Stay Consistent <b>with MB</b> in Your Pocket!</p>
  </section>

  <section class="card" style="left:721px;top:304px">
    <div class="ghost" style="left:140px;top:20px;width:80px;height:55px"></div>
    <div class="ghost" style="left:10px;top:130px;width:70px;height:50px;transform:rotate(-10deg)"></div>
    <h2 class="headline center" style="top:22px;font-size:33.5px;line-height:1.06">Eat<br>the food<br>you love.<br><em class="accent">Stay<br>accountable<br>every day.</em></h2>
    <p class="tagline" style="top:264px">Stay Consistent <b>with MB</b> in Your Pocket!</p>
  </section>

  <section class="card" style="left:958px;top:304px">
    <div class="ghost" style="left:10px;top:60px;width:60px;height:55px;transform:rotate(-10deg)"></div>
    <div class="ghost" style="left:145px;top:15px;width:80px;height:55px"></div>
    <div class="photo photo--duo" role="img" aria-label="Photo: two women laughing together in denim jackets" style="left:36px;top:12px;width:150px;height:165px"></div>
    <h2 class="headline center" style="top:171px;font-size:25px;line-height:1.08">One Bad Meal<br><span class="accent">Doesn't Mean<br>You Failed</span></h2>
    <p class="tagline" style="top:264px">Stay Consistent <b>with MB</b> in Your Pocket!</p>
  </section>

</main>
</body>
</html>
```